Web Design + logo Project

hi,
we are based in ASEAN region (Malaysia/Indonesia/Singapore), involving in Online Vehicle Insurance Portal. so far our product is only car insurance and personal insurance, and motorbikes insurance)
We need a webdesign + logo for TolaKover.com
The website is www.tolakover.example. The website is already up with the necessary quotation comparison + purchase mechanism.
We like www.brightlane.example look and feel very much.
Blue is the preferred main theme.
The mainpage should highlight the following
1) quotation generator/input
2) hotline number
3) news/testimonial
The webdesign should be able to cater for mobile users as well.
The design should be professional and energetic
Target Market(s)
20-35years old vehicle owners in Indonesia/thailand/Singapore/vietnam
Industry/Entity Type
Car Insurance
Look and feel

```html
<!DOCTYPE html>
<html lang="en">
<head>
<meta charset="utf-8">
<title>TolaKover – Online Vehicle Insurance</title>
<link href="https://fonts.googleapis.com/css2?family=PT+Sans:ital,wght@0,400;0,700;1,400&family=PT+Sans+Narrow:wght@400;700&family=Arimo:ital,wght@0,400;1,400;1,700&family=Archivo+Black&display=swap" rel="stylesheet">
<style>
:root{
  --blue:#1f8fd6;
  --blue-dark:#1469a8;
  --blue-deep:#0f5a93;
  --blue-text:#1a74bd;
  --ink:#1c1c1c;
  --grey:#6d6d6d;
  --line:#bcbcbc;
  --bar-top:#bdbdbd;
  --bar-bot:#8e8e8e;
  --red:#d8332a;
}
*{box-sizing:border-box;margin:0;padding:0}
html,body{width:1200px;height:1170px;overflow:hidden;background:#fff}
.page{position:relative;width:1200px;height:1170px;font-family:"PT Sans",sans-serif;color:var(--ink)}
.abs{position:absolute}

/* header */
.brand{left:116px;top:52px;display:flex;align-items:center;gap:12px}
.brand-mark{width:58px;height:58px;border-radius:50%;background:var(--blue-dark)}
.brand-name{font-family:"PT Sans",sans-serif;font-weight:700;font-size:40px;color:var(--blue);letter-spacing:.5px}
.hotline{right:118px;top:38px;display:flex;align-items:center;gap:10px;font-family:"PT Sans",sans-serif;font-size:15px;color:#8a8a8a}
.main-nav{left:448px;top:73px;width:642px;height:34px;background:linear-gradient(#9a9a9a,#6e6e6e);clip-path:polygon(10px 0,100% 0,100% 100%,0 100%);display:flex;align-items:center;justify-content:space-around;padding-left:14px}
.main-nav a{font-family:"Arimo",sans-serif;font-style:italic;font-size:11.5px;color:#fff;text-decoration:none;text-transform:uppercase}

/* hero */
.hero{left:110px;top:122px;width:710px;height:385px}
.hero-art{left:380px;top:135px;width:430px;height:365px;background:radial-gradient(circle at 65% 40%,#f1e3d8 0,#c9a48a 18%,#b86a3d 40%,#3c97d6 70%);opacity:.9;clip-path:polygon(0 40%,55% 0,100% 0,100% 100%,0 100%)}
.hero-title{left:222px;top:206px;font-family:"Archivo Black",sans-serif;font-size:36px;color:#fff;letter-spacing:1px}
.hero-band{left:110px;top:243px;width:352px;height:38px}
.hero-band span{position:absolute;left:34px;top:5px;font-family:"PT Sans Narrow",sans-serif;font-weight:700;font-style:italic;font-size:25px;color:#111;transform:skewX(-8deg)}
.hero-sub{left:143px;top:292px;font-family:"PT Sans Narrow",sans-serif;font-weight:700;font-size:19px;color:#fff;font-style:italic;transform:skewX(-6deg)}
.hero-copy{left:140px;top:322px;width:250px;font-family:"Arimo",sans-serif;font-style:italic;font-size:12px;line-height:18px;color:#111}
.slider-dots{left:746px;top:482px;display:flex;gap:3px}
.slider-dots i{width:8px;height:8px;background:#fff}
.slider-dots i.on{background:var(--red)}

/* quote panel */
.quote{left:810px;top:122px;width:280px;height:395px}
.quote-form{left:845px;top:158px;width:220px;font-family:"Arimo",sans-serif;font-size:10.5px;color:#fff}
.quote-title{font-family:"PT Sans Narrow",sans-serif;font-weight:700;font-style:italic;font-size:26px;color:#fff;margin:0 0 10px -4px;transform:scaleX(.95);transform-origin:left}
.q-label{margin-top:4px;height:15px}
.q-field{height:18px;background:#fff;color:#888;font-size:10px;line-height:18px;padding-left:7px;position:relative;margin-bottom:6px}
.q-field b{position:absolute;right:1px;top:2px;width:14px;height:14px;border:1px solid #999;background:#eee}
.q-field b::after{content:"";position:absolute;left:3px;top:4px;border:4px solid transparent;border-top:5px solid #333}
.q-checks{display:flex;gap:16px;margin:5px 0 8px 2px}
.q-checks span{display:flex;align-items:center;gap:5px}
.box{width:11px;height:11px;background:#fff;border:1px solid #aaa;display:inline-block;position:relative}
.box.on::after{content:"";position:absolute;left:3px;top:0;width:3px;height:7px;border:solid #333;border-width:0 2px 2px 0;transform:rotate(40deg)}
.truck-art{left:918px;top:400px;width:168px;height:115px;background:linear-gradient(90deg,#c9ced4 0,#e6e9ec 45%,#b3202c 60%,#8f1620 100%);border-radius:4px}

/* category buttons */
.cats{left:119px;top:541px;display:flex;gap:10px}
.cat{width:232px;height:56px;background:linear-gradient(#ffffff,#ececec);border:1px solid #dcdcdc;border-radius:3px;display:flex;align-items:center;box-shadow:0 3px 4px rgba(0,0,0,.08)}
.cat-icon{width:58px;height:100%;border-right:1px solid #d6d6d6;display:flex;align-items:center;justify-content:center}
.cat-label{padding-left:17px;font-family:"PT Sans Narrow",sans-serif;font-size:23px;color:#222}

.dots{left:122px;width:955px;border-top:1px dotted #9a9a9a}

/* intro */
.intro-h{left:119px;top:655px;font-family:"PT Sans Narrow",sans-serif;font-size:23px;color:#111}
.intro-h em{font-style:normal;color:var(--blue-text);font-size:27px;margin-left:6px}
.intro-p{left:119px;top:694px;width:960px;font-size:13px;line-height:20px;color:#111}
.list{font-size:13.5px;color:var(--blue-text)}
.list li{list-style:none;height:30px;display:flex;align-items:center;gap:17px}
.bullet{width:13px;height:13px;border-radius:50%;background:linear-gradient(#fff,#ddd);border:1px solid #c4c4c4;position:relative;flex:none}
.bullet::after{content:"";position:absolute;left:4px;top:3px;border:3px solid transparent;border-left:4px solid #666}

/* news */
.news-h{left:124px;top:853px;font-family:"PT Sans Narrow",sans-serif;font-size:22px;color:var(--blue-text);display:flex;align-items:center;gap:12px}
.news-bar{left:271px;top:850px;width:808px;height:30px;background:linear-gradient(#2ea0e6,#1580cf);border-radius:3px;display:flex;align-items:center;color:#fff;font-size:12.5px;white-space:nowrap;overflow:hidden}
.news-bar span{display:flex;align-items:center;gap:14px;padding-left:10px}
.news-bar span::before{content:"";border:4px solid transparent;border-left:5px solid #fff}
.news-bar span+span{border-left:1px solid #5cb7ee}

/* renew & newsletter */
.sec-h{font-family:"PT Sans Narrow",sans-serif;font-size:17px;color:var(--blue-text);text-transform:uppercase}
.renew-list{font-size:13.5px;color:#111}
.vrule{left:651px;top:925px;height:99px;border-left:1px solid #b5b5b5}
.email{left:724px;top:963px;width:352px;height:31px;border:1px solid #b5b5b5;font-size:12px;color:#666;padding:7px 0 0 8px}
.signup{left:1013px;top:1005px;width:65px;height:24px;background:linear-gradient(#1c85cf,#0d5ea0);color:#fff;border-radius:3px;font-size:13px;text-align:center;line-height:24px}

/* footer */
.foot-nav{left:110px;top:1056px;width:980px;height:41px;display:flex;background:linear-gradient(var(--bar-top),var(--bar-bot))}
.foot-nav a{font-family:"Arimo",sans-serif;font-style:italic;font-size:14px;color:#fff;text-decoration:none;display:flex;align-items:center;justify-content:center;border-right:1px solid #d8d8d8}
.copy{left:120px;top:1111px;font-family:"Arimo",sans-serif;font-style:italic;font-size:10px;color:#555}
.follow{left:886px;top:1110px;display:flex;align-items:center;gap:6px;font-family:"Arimo",sans-serif;font-size:11px;color:#333}
.follow i{width:25px;height:28px;border-radius:3px;background:linear-gradient(#4aa0e0,#1c5f9f);display:inline-block}
.follow i.r{background:linear-gradient(#e0e0e0,#a8a8a8)}
</style>
</head>
<body>
<div class="page">

  <header>
    <div class="abs brand">
      <span class="brand-mark"></span>
      <span class="brand-name">TolaKover</span>
    </div>
    <div class="abs hotline">Call Us At: 0000 000 000
      <svg width="26" height="30" viewBox="0 0 26 30"><path d="M18 2l5 3-3 7-4-1c-2 4-4 9-5 12l4 2-2 4-6-2C6 21 10 9 18 2z" fill="#c8252c"/></svg>
    </div>
    <nav class="abs main-nav">
      <a href="#">Home</a><a href="#">About Us</a><a href="#">Insurance Choices</a><a href="#">Claims Center</a><a href="#">Customer Service</a><a href="#">Contact Us</a>
    </nav>
  </header>

  <section>
    <svg class="abs hero" viewBox="0 0 710 385">
      <defs><linearGradient id="heroBg" x1="0" y1="0" x2="1" y2="1"><stop offset="0" stop-color="#2a9ae0"/><stop offset="1" stop-color="#1680cc"/></linearGradient></defs>
      <polygon points="0,20 700,0 700,383 0,363" fill="url(#heroBg)"/>
    </svg>
    <div class="abs hero-art" role="img" aria-label="Photo of a smiling woman standing beside an orange compact SUV in front of a city highway at dusk"></div>
    <div class="abs hero-title">ARSAGUNA</div>
    <svg class="abs hero-band" viewBox="0 0 352 38"><polygon points="0,0 337,0 352,19 337,38 0,38" fill="#fff"/></svg>
    <div class="abs hero-band" style="background:none"><span>VEHICLE INSURANCE COMPANY</span></div>
    <div class="abs hero-sub">INSURANCE FOR ALL VEHICLES</div>
    <p class="abs hero-copy">Lorem Ipsum is simply dummy text of the printing and typesetting industry. Lorem Ipsum has been the industry's standard dummy text ever since the 1500s,</p>
    <div class="abs slider-dots"><i class="on"></i><i></i><i></i><i></i><i></i></div>

    <svg class="abs quote" viewBox="0 0 280 395">
      <defs><linearGradient id="quoteBg" x1="0" y1="0" x2="0" y2="1"><stop offset="0" stop-color="#1a72b4"/><stop offset="1" stop-color="#2d8ccd"/></linearGradient></defs>
      <polygon points="0,14 280,0 280,392 0,380" fill="url(#quoteBg)"/>
    </svg>
    <form class="abs quote-form">
      <div class="quote-title">CEK PREMI</div>
      <div class="q-label">Jenis Kendaraan:</div>
      <div class="q-field">- Pilih Jenis -<b></b></div>
      <div class="q-label">Tahun:</div>
      <div class="q-field">- Pilih Jenis -<b></b></div>
      <div class="q-label">Harga Pertanggungan</div>
      <div class="q-field">- 100.000.000 -</div>
      <div class="q-label">Kategori:</div>
      <div class="q-checks"><span><i class="box on"></i>Pribadi</span><span style="margin-left:14px"><i class="box"></i>Dinas</span></div>
      <div class="q-label" style="margin-top:-4px">Pertanggungan:</div>
      <div class="q-checks"><span><i class="box on"></i>Total Loss Only</span><span style="margin-left:-8px"><i class="box"></i>Comprehensive</span></div>
    </form>
    <div class="abs truck-art" role="img" aria-label="Photo of a red cargo truck with a white trailer"></div>
  </section>

  <div class="abs cats">
    <div class="cat"><div class="cat-icon"><svg width="30" height="30" viewBox="0 0 30 30"><path d="M7 6h16l3 9v10h-4v-3H8v3H4V15z" fill="#1d6fb5"/><rect x="9" y="9" width="12" height="5" fill="#fff"/><circle cx="9" cy="18" r="2" fill="#fff"/><circle cx="21" cy="18" r="2" fill="#fff"/></svg></div><span class="cat-label">Motor Insurance</span></div>
    <div class="cat"><div class="cat-icon"><svg width="40" height="28" viewBox="0 0 40 28"><circle cx="9" cy="19" r="7" fill="none" stroke="#1d5f9f" stroke-width="3"/><circle cx="31" cy="19" r="7" fill="none" stroke="#1d5f9f" stroke-width="3"/><path d="M9 19l8-8h10l4 8" fill="none" stroke="#1d5f9f" stroke-width="3"/><rect x="14" y="6" width="12" height="6" rx="2" fill="#1d5f9f"/></svg></div><span class="cat-label">Motorbike Insurance</span></div>
    <div class="cat"><div class="cat-icon"><svg width="34" height="40" viewBox="0 0 34 40"><circle cx="15" cy="10" r="7" fill="#c58e6a"/><path d="M3 36c0-10 5-15 12-15s12 5 12 15z" fill="#3f7fc0"/><circle cx="25" cy="30" r="7" fill="#1966b0"/><rect x="24" y="28" width="2" height="6" fill="#fff"/><rect x="24" y="25" width="2" height="2" fill="#fff"/></svg></div><span class="cat-label">Personal Insurance</span></div>
    <div class="cat"><div class="cat-icon"><svg width="26" height="26" viewBox="0 0 26 26"><path d="M13 4H4v18h18v-9" fill="none" stroke="#1d6fb5" stroke-width="3"/><path d="M10 16l2-5 9-9 3 3-9 9z" fill="#1d6fb5"/></svg></div><span class="cat-label">Claims Center</span></div>
  </div>

  <div class="abs dots" style="top:631px"></div>

  <h1 class="abs intro-h">Buy Online Vehicle Insurance from<em>TolaKover</em></h1>
  <p class="abs intro-p">Your vehicle insurance is about freedom and the Arsaguna vehicle insurance policy has been designed to set you free. Our comprehensive vehicleinsurance policy provides hassle-free protection to your bike or scooter against physical damage, theft and third party liability.</p>
  <ul class="abs list" style="left:153px;top:747px"><li><i class="bullet"></i>Cashless settlement in preferred workshops</li><li><i class="bullet"></i>Hassle-free claim settlement</li></ul>
  <ul class="abs list" style="left:555px;top:747px"><li><i class="bullet"></i>Quick and easy steps to purchase online</li><li><i class="bullet"></i>24x7 claim support</li></ul>

  <div class="abs dots" style="top:831px"></div>

  <div class="abs news-h">LATEST NEWS
    <svg width="24" height="14" viewBox="0 0 24 14"><path d="M0 7h22M16 1l6 6-6 6" fill="none" stroke="#333" stroke-width="1.5"/></svg>
  </div>
  <div class="abs news-bar">
    <span style="width:268px">Insure yours cards against loss or misuse</span>
    <span style="width:322px">Know your Policy Before Buying Health Insurance</span>
    <span>Insure yours cards against loss or</span>
  </div>

  <div class="abs dots" style="top:902px"></div>

  <h2 class="abs sec-h" style="left:126px;top:926px">Want to renew your vehicle insurance?</h2>
  <ul class="abs renew-list" style="left:138px;top:958px"><li class="list-item" style="list-style:none;height:30px;display:flex;align-items:center;gap:14px"><i class="bullet"></i>Extra protection through 8 add on covers</li><li style="list-style:none;height:30px;display:flex;align-items:center;gap:14px"><i class="bullet"></i>7 days claims settlement service</li></ul>
  <ul class="abs renew-list" style="left:441px;top:960px"><li style="list-style:none;height:30px;display:flex;align-items:center;gap:14px"><i class="bullet"></i>Free Car Pick Up</li><li style="list-style:none;height:30px;display:flex;align-items:center;gap:14px"><i class="bullet"></i>Warranty on Repairs</li></ul>

  <div class="abs vrule"></div>

  <h2 class="abs sec-h" style="left:722px;top:926px">Newsletter Signup</h2>
  <div class="abs email">Enter the E mail id</div>
  <div class="abs signup">Sign Up</div>

  <footer>
    <nav class="abs foot-nav">
      <a href="#" style="width:240px">INSURANCE CHOICES</a>
      <a href="#" style="width:239px">CLAIMS CENTER</a>
      <a href="#" style="width:291px">CUSTOMER SERVICE</a>
      <a href="#" style="width:210px;border-right:0">CONTACT US</a>
    </nav>
    <p class="abs copy">Copyright © 2012 Tolakover All rights reserved</p>
    <div class="abs follow">FOLLOW US :
      <span style="display:flex;gap:5px;margin-left:4px"><i></i><i></i><i></i><i class="r"></i></span>
    </div>
  </footer>

</div>
</body>
</html>
```